Easter. Company for collection, treatment and recovery of dangerous and dangerous goods. not dangerous

We need an image folder with 4 pages, details see insert, logo can not be changed and some pictures collection and treatment of hazardous and non-hazardous waste, Tankwageninnenreinigung own fleet

Target Market(s)

existing customers and new customers

Colors

Designer to choose colors to be used in the design.

Requirements
Must have
• KARVO logo
Nice to have
• Design the text and the pictures so that it suits our disposal company. You can also use the pictures from our webside.

```html
<!DOCTYPE html>
<html lang="de">
<head>
<meta charset="utf-8">
<title>KARVO – Wir schließen den Kreislauf</title>
<link href="https://fonts.googleapis.com/css2?family=Raleway:wght@300;500;700&family=Roboto+Condensed:wght@400;700&family=Open+Sans:wght@400;600&display=swap" rel="stylesheet">
<style>
  :root{
    --green:#1f7a45;
    --green-dark:#1c5a35;
    --grey-band:#9aa3a0;
    --grey-dark:#4b4f4e;
    --ink:#333;
    --paper:#ffffff;
    --backdrop:#a9afac;
  }
  *{box-sizing:border-box;margin:0;padding:0}
  html,body{width:1200px;height:824px;overflow:hidden}
  body{background:var(--backdrop);font-family:"Open Sans",sans-serif;color:var(--ink);position:relative}
  .page{position:absolute;top:22px;width:552px;height:780px;background:var(--paper);overflow:hidden;box-shadow:0 4px 18px rgba(0,0,0,.25)}
  .page--back{left:44px}
  .page--front{left:604px}

  .brand{display:flex;align-items:center;justify-content:center;gap:8px}
  .brand__dot{width:14px;height:14px;border-radius:50%}
  .brand__name{font-family:"Raleway",sans-serif;font-weight:700;font-size:30px;letter-spacing:2px;line-height:1}
  .brand__tag{font-family:"Raleway",sans-serif;font-weight:500;font-size:8px;letter-spacing:2.5px;text-align:center;margin-top:8px}

  /* back cover */
  .back__header{height:128px;background:var(--green);padding-top:42px;color:#fff}
  .back__header .brand__dot{background:#fff}
  .back__header .brand__name{color:#fff}
  .back__strip{height:8px;background:var(--grey-band)}
  .back__photo{height:374px;background:linear-gradient(180deg,#8fa3bd 0%,#c9d3de 38%,#5d6a78 62%,#2e3d4f 100%)}
  .back__info{display:flex;padding:20px 26px 0 26px;gap:22px;align-items:flex-start}
  .back__text{flex:1;font-size:10.5px;line-height:1.6;text-align:left}
  .badges{display:grid;grid-template-columns:repeat(2,74px);gap:10px;flex:none}
  .badge{height:48px;border:1px solid #ccc;display:flex;align-items:center;justify-content:center}
  .badge span{width:30px;height:30px;border-radius:50%;background:#e07a2b}
  .badge--blue span{background:#2f6db3}
  .badge--green span{background:var(--green);border-radius:4px;width:44px;height:22px}
  .contacts{display:grid;grid-template-columns:1fr 1fr;gap:6px 16px;padding:16px 26px 0;font-size:10.5px;font-weight:600}
  .contacts li{list-style:none;display:flex;align-items:center;gap:6px;white-space:nowrap}
  .contacts svg{width:11px;height:11px;fill:var(--green);flex:none}
  .back__footer{position:absolute;left:0;right:0;bottom:0;height:20px;background:var(--grey-dark)}
  .back__footer::before{content:"";position:absolute;left:0;right:0;top:-5px;height:5px;background:var(--grey-band)}

  /* front cover */
  .front__head{padding-top:34px;height:116px}
  .front__head .brand__dot{background:var(--green)}
  .front__head .brand__name{color:var(--green)}
  .front__head .brand__tag{color:var(--grey-dark)}
  .front__photo{height:356px;background:linear-gradient(170deg,#c8d2dc 0%,#7b97b0 22%,#6f8a55 45%,#4c7a2c 70%,#7a4a2a 100%)}
  .front__band{height:58px;background:linear-gradient(90deg,var(--green-dark),var(--green));color:#fff;font-family:"Raleway",sans-serif;font-weight:300;font-size:27px;letter-spacing:1.5px;display:flex;align-items:center;padding-left:30px;white-space:nowrap}
  .services{display:grid;grid-template-columns:1fr 1.25fr;gap:0 20px;padding:26px 36px 0;font-family:"Roboto Condensed",sans-serif;font-weight:700;font-size:13px}
  .services ul{list-style:none}
  .services li{display:flex;align-items:flex-start;gap:8px;margin-bottom:6px;line-height:1.2}
  .services svg{width:16px;height:10px;flex:none;margin-top:3px;stroke:var(--grey-dark);fill:none;stroke-width:1.6}
  .front__web{text-align:center;margin-top:24px;font-size:10px;letter-spacing:5px}
  .front__footer{position:absolute;left:0;right:0;bottom:0;height:20px;background:var(--green-dark)}
  .front__footer::before{content:"";position:absolute;left:0;right:0;top:-5px;height:5px;background:var(--grey-band)}
</style>
</head>
<body>
  <section class="page page--back">
    <header class="back__header">
      <div class="brand"><span class="brand__dot"></span><span class="brand__name">KARVO</span></div>
      <p class="brand__tag">WIR SCHLIESSEN DEN KREISLAUF</p>
    </header>
    <div class="back__strip"></div>
    <div class="back__photo" role="img" aria-label="Firmengelände mit Hallen, Tankwagen und Lkw unter bewölktem Himmel"></div>
    <div class="back__info">
      <p class="back__text">Die KARVO Entsorgung und Rohstoffkreislauf GmbH ist ein modernes, mittelständisches Dienstleistungsunternehmen im Großraum Südwestbayern, das mit zeitgemäßer Verfahrenstechnik eine Vielzahl an Lösungen rund um Entsorgung, Recycling und die Innenreinigung von Tankwagen anbietet. KARVO ist seit 1991 am Standort Gewerbestraße 12 in Lindau tätig.</p>
      <div class="badges">
        <div class="badge badge--green"><span></span></div>
        <div class="badge"><span></span></div>
        <div class="badge"><span></span></div>
        <div class="badge badge--blue"><span></span></div>
      </div>
    </div>
    <ul class="contacts">
      <li><svg viewBox="0 0 12 12"><path d="M2 1l2 0 1 3-1.5 1a7 7 0 0 0 3.5 3.5L8 7l3 1v2a1 1 0 0 1-1 1A9 9 0 0 1 1 2a1 1 0 0 1 1-1z"/></svg>0049/8382/55120</li>
      <li><svg viewBox="0 0 12 12"><path d="M1 3h10v7H1z M1 3l5 4 5-4"/></svg>info@karvo-kreislauf.de</li>
      <li><svg viewBox="0 0 12 12"><rect x="1" y="4" width="10" height="6" rx="1"/><rect x="3" y="1" width="6" height="3"/></svg>0049/8382/55129</li>
      <li><svg viewBox="0 0 12 12"><circle cx="6" cy="6" r="5"/></svg>www.karvo-kreislauf.de</li>
    </ul>
    <div class="back__footer"></div>
  </section>

  <section class="page page--front">
    <header class="front__head">
      <div class="brand"><span class="brand__dot"></span><span class="brand__name">KARVO</span></div>
      <p class="brand__tag">WIR SCHLIESSEN DEN KREISLAUF</p>
    </header>
    <div class="front__photo" role="img" aria-label="Reisterrassen in grüner Berglandschaft im Gegenlicht der Sonne"></div>
    <h1 class="front__band">WIR SCHLIESSEN DEN KREISLAUF</h1>
    <div class="services">
      <ul>
        <li><svg viewBox="0 0 16 10"><path d="M1 9Q8 9 15 1"/></svg>Abfallsammlung</li>
        <li><svg viewBox="0 0 16 10"><path d="M1 9Q8 9 15 1"/></svg>Abfallbehandlung</li>
        <li><svg viewBox="0 0 16 10"><path d="M1 9Q8 9 15 1"/></svg>Abfallentsorgung</li>
      </ul>
      <ul>
        <li><svg viewBox="0 0 16 10"><path d="M1 9Q8 9 15 1"/></svg>Reinigung von Industrieanlagen und Behälter</li>
        <li><svg viewBox="0 0 16 10"><path d="M1 9Q8 9 15 1"/></svg>Tankwageninnenreinigung</li>
      </ul>
    </div>
    <p class="front__web">www.karvo-kreislauf.de</p>
    <div class="front__footer"></div>
  </section>
</body>
</html>
```